Guaranteed Job - Sleek Sexy Business Card UV Spot

Im looking for a sleek and sexy business card, that resembles elite or VIP status status.
our business is corinvale.example
you can view our products on there, but our main audience for handing out our cards will be for people in the hospitality industry, so it will need to impress high management and CEO of hotels and restaurants, bars, clubs etc...
the card features will have UV spot on both sides, 400gsm stock. standard size.
Artwork should be 86 x 54mm + 2mm bleed = 90 x 58mm
it should have a nice "unique" uv spot pattern that highlights the card, not a repeated pattern, theres no originality there, and it will be disregarded.
The written material will be:
Corin Vale Hospitality College (logo)
Tobin Marsh
Director
Phone: 1300 615 737
Mobile: 0455 817 296
Email: info@corinvale.example
website: www.corinvale.example
I'm looking for originality here, i don't want just a simple stock card, want something that has a wow factor for people.
You will find the logo attached. you may invert the white to black words to suit the background as you please.
thank you and good luck
As a side note, ive received a lot of proposals, im too busy to give feedback to each and every one, so if i havent provided feedback for your design within 24 hours, then consider it not acceptable, and you could resubmit another design.
So far i have not seen any design that stood out for me, they all seem pretty generic. there nothing thats unique, i would figure for the amount that im offering, that people would put some more effort and creativity into the design.
so far over 200 designs submitted, and nothing i have seen looks very original, everything looks like a different variation of the same stuff, i said it very clearly i wanted something unique, the only thing that has come close to it so far is this one
Reason: Ive received alot of design concepts and i have reviewed everyone, but i havent had time to give feedback to every single one, only the ones that have interested me, if i havent responded, its because i havent found it good enough.
so far only a few design have been on par with what ive been looking for, an attractive eye popping design.
heres a few of them,
http://files.pixelbazaar.example/design_img/51736/62418/62418_2840915_51736_image.jpg
http://files.pixelbazaar.example/design_img/51736/68254/68254_2841377_51736_image.jpg
theyre, both unique and original, and eye catching, the only thing theyre missing is the sexyness.
if you still think you have some creativity left in your minds, then throw it on here.
Reason: Sorry guys for the delay, I was in a serious accident and out of commission for the past few months, I'm just slowly recovering now, please bare with me as i try to attend to this project, it may take me awhile as I have other projects that are on standby, I'm not 100% at the moment, so im extending the deadline for 2 weeks right now. Thanks for your patience.
Hospitality

```html
<!DOCTYPE html>
<html lang="en">
<head>
<meta charset="utf-8">
<title>Corin Vale Hospitality College – Business Card</title>
<link rel="stylesheet" href="https://fonts.googleapis.com/css2?family=Questrial&display=swap">
<style>
  :root {
    --card-black: #000000;
    --pattern-grey: #1a1a1a;
    --pattern-edge: #0b0b0b;
    --accent-blue: #5ab4e5;
    --contact-teal: #14b2a2;
    --label-white: #f2f2f2;
    --chrome-light: #ffffff;
    --chrome-mid: #b9c6cf;
    --chrome-dark: #4f5a61;
  }
  * { margin: 0; padding: 0; box-sizing: border-box; }
  html, body {
    width: 1200px;
    height: 773px;
    overflow: hidden;
    background: var(--card-black);
  }
  .card {
    position: relative;
    width: 1200px;
    height: 773px;
    background: var(--card-black);
    font-family: "Questrial", "Century Gothic", sans-serif;
    overflow: hidden;
  }
  .uv-pattern {
    position: absolute;
    left: 327px;
    top: 23px;
    width: 873px;
    height: 727px;
  }
  .brand {
    position: absolute;
    left: 40px;
    top: 300px;
    width: 260px;
  }
  .brand-mark {
    width: 40px;
    height: 40px;
    background: var(--accent-blue);
    margin-bottom: 22px;
  }
  .brand-name {
    color: var(--accent-blue);
    font-size: 30px;
    font-weight: 400;
    line-height: 1.25;
  }
  .identity {
    position: absolute;
    left: 277px;
    width: 800px;
    text-align: center;
    font-size: 90px;
    font-weight: 400;
    line-height: 1;
    background: linear-gradient(180deg, var(--chrome-light) 0%, var(--chrome-mid) 45%, var(--chrome-dark) 55%, var(--chrome-light) 100%);
    -webkit-background-clip: text;
    background-clip: text;
    color: transparent;
  }
  .person-name { top: 86px; }
  .person-title { top: 227px; }
  .contact {
    position: absolute;
    left: 283px;
    width: 800px;
    text-align: center;
    font-size: 50px;
    line-height: 1;
    color: var(--label-white);
    white-space: nowrap;
  }
  .contact .initial { color: var(--accent-blue); }
  .contact .value { color: var(--contact-teal); }
  .contact-phone { top: 383px; }
  .contact-mobile { top: 451px; }
  .contact-email { top: 587px; }
  .contact-web { top: 654px; }
</style>
</head>
<body>
<main class="card">
  <svg class="uv-pattern" viewBox="0 0 873 727" role="img" aria-label="Unique UV spot pattern of interlocking rounded shapes and circles">
    <defs>
      <radialGradient id="uvGlow" cx="50%" cy="45%" r="65%">
        <stop offset="0%" stop-color="#1a1a1a"/>
        <stop offset="100%" stop-color="#0b0b0b"/>
      </radialGradient>
    </defs>
    <rect width="873" height="727" fill="url(#uvGlow)"/>
  </svg>

  <div class="brand">
    <div class="brand-mark"></div>
    <p class="brand-name">Corin Vale<br>Hospitality<br>College</p>
  </div>

  <h1 class="identity person-name">Tobin Marsh</h1>
  <p class="identity person-title">Director</p>

  <p class="contact contact-phone"><span class="initial">P</span>hone: <span class="value">1300 615 737</span></p>
  <p class="contact contact-mobile"><span class="initial">M</span>obile: <span class="value">0455 817 296</span></p>
  <p class="contact contact-email"><span class="initial">E</span>mail: <span class="value">info@corinvale.example</span></p>
  <p class="contact contact-web"><span class="initial">w</span>ebsite: <span class="value">www.corinvale.example</span></p>
</main>
</body>
</html>
```